Commercial Construction Company Looking to Revamp Image

Varnholt Construction Co., Inc. has been in business for 20 years, and is a mid sized commercial construction company looking to update our image to reflect a more modern corporate culture, but to still reflect traditional core values in construction, such as dependability, honesty, and solid workmanship. Our largest clients include government and public agencies who seek companies with the aforementioned values, but are open to new ideas and innovations. We have used a dark blue and white to represent us in the past and would like for this color scheme to continue as not to isolate our existing customers. The addition of a gray is acceptable. Please see our previous business card. *It is imperative to retain the logo as closely as possible.* There is a possibility to shorten the name of the company to "VCCI," dependent on design concepts, or possible integration of the acronym to our existing name.

Industry/Entity Type

Business

```html
<!DOCTYPE html>
<html lang="en">
<head>
<meta charset="utf-8">
<title>Varnholt Construction Co., Inc. — Business Cards</title>
<link rel="stylesheet" href="https://fonts.googleapis.com/css2?family=Poiret+One&family=Questrial&display=swap">
<style>
  :root {
    --stage: #3d3e44;
    --stage-light: #4a4b52;
    --card-edge: #9daefc;
    --card-mid: #d6dcfb;
    --card-center: #f4f5fd;
    --brand-blue: #2f45e6;
    --mark-blue: #4a68f2;
    --mark-text: #ffffff;
  }
  * { box-sizing: border-box; margin: 0; padding: 0; }
  html, body { width: 1200px; height: 1000px; overflow: hidden; }
  body {
    position: relative;
    background: radial-gradient(ellipse at 70% 70%, var(--stage-light), var(--stage) 70%);
    font-family: "Poiret One", sans-serif;
    color: var(--brand-blue);
  }
  .card {
    position: absolute;
    width: 833px;
    height: 426px;
    background: radial-gradient(ellipse at 50% 45%, var(--card-center) 0%, var(--card-mid) 50%, var(--card-edge) 100%);
    box-shadow: 0 10px 40px rgba(0,0,0,0.55);
  }
  .card--front { left: 348px; top: 30px; }
  .card--back { left: 32px; top: 547px; }

  .address, .contacts {
    position: absolute;
    top: 16px;
    font-size: 17px;
    line-height: 21px;
    font-weight: 700;
    letter-spacing: 0.2px;
  }
  .address { left: 11px; }
  .contacts { right: 34px; top: 22px; text-align: right; }

  .brand-mark {
    position: absolute;
    background: var(--mark-blue);
    border-radius: 4px;
    display: flex;
    align-items: center;
    justify-content: center;
    color: var(--mark-text);
    font-family: "Poiret One", sans-serif;
    font-weight: 400;
  }
  .card--front .brand-mark { left: 338px; top: 10px; width: 144px; height: 122px; font-size: 40px; }
  .card--back .brand-mark { left: 316px; top: 28px; width: 221px; height: 230px; font-size: 62px; }

  .company {
    position: absolute;
    left: 0; right: 0;
    text-align: center;
    text-transform: uppercase;
    line-height: 1;
    font-weight: 400;
  }
  .company small { font-size: 0.55em; }
  .card--front .company { top: 148px; padding-left: 0; margin-left: 0; }
  .card--front .company .line-1 { font-size: 27px; letter-spacing: 1px; }
  .card--front .company .line-2 { font-size: 31px; margin-top: 2px; }
  .card--back .company { top: 288px; left: -60px; }
  .card--back .company .line-1 { font-size: 45px; letter-spacing: 2px; }
  .card--back .company .line-2 { font-size: 50px; margin-top: 8px; }

  .person {
    position: absolute;
    left: 0; right: 0;
    top: 214px;
    text-align: center;
    font-family: "Questrial", sans-serif;
    font-size: 50px;
    line-height: 62px;
  }
</style>
</head>
<body>
  <section class="card card--front" aria-label="Card front">
    <address class="address">
      1842 Halden Avenue<br>
      &nbsp;Jersey City, N.J. 07305<br>
      varnholtbuild@mailbox.com
    </address>
    <div class="brand-mark">VCCI</div>
    <div class="contacts">
      Office: (201) 555-0142<br>
      Fax: (201) 555-0187<br>
      Cell: (917) 555-0163
    </div>
    <h1 class="company">
      <div class="line-1">Varnholt</div>
      <div class="line-2">Construction <small>Co., Inc</small></div>
    </h1>
    <div class="person">
      <div class="person-name">Marek Varnholt</div>
      <div class="person-title">President</div>
    </div>
  </section>

  <section class="card card--back" aria-label="Card back">
    <div class="brand-mark">VCCI</div>
    <h2 class="company">
      <div class="line-1">Varnholt</div>
      <div class="line-2">Construction <small>Co., Inc</small></div>
    </h2>
  </section>
</body>
</html>
```